依頼詳細
シンプルかつスタイリッシュで、落ち着いたデザインを希望します。弊社イメージカラーはオレンジですが、建物との統一性を持たせたカラー(紺色:写真参照)のほうが良いかと思っています。(オレンジを使用していただいても結構です)
サイズや表記内容等は「記載項目」をご覧ください。
記載項目
クロベリアルティ株式会社
クロベリーガル事務所またはクロベリーガル行政書士|土地家屋調査士事務所(バランス等考慮し、どちらかを選択)は必須ですが、電話番号は必要ありません。
また、ロゴマークも必須ですが、マークの選択はお任せします。(添付ファイル参照)
また、事業内容については参考に名刺を添付しますが、多くの情報を入れることは望みません。事業所名をクロベリーガル事務所とする場合は、行政書士及び土地家屋調査士を事業内容としていただいても結構です。
寸法につきましては、添付ファイルをご確認ください。

希望イメージ
シンプル 複雑
単色 カラフル
暗い 明るい
日常 高級
遊び心 厳粛
未来的 伝統的
女性的 男性的
希望する色
事務所看板のため、建物と統一性のあるものにしたいです
納品ファイル
• イラストレーター形式 (.ai)
補足説明
事業内容は必ずしも記載しなければならないものではありません。(どちらでもよいです)
■ 選んだ理由

「シンプルでスタイリッシュ」の希望を見事に叶えていただきました。
中でもロゴの配置が絶妙で、色合いも素晴らしかったです。

■ 提案者全員のお礼・コメント

この度は弊社コンペにご参加いただきまして、誠にありがとうございました。
レベルが高く秀逸な作品が多いため選定に悩みましたが、嬉しい悲鳴で選定を楽しませていただきました。
今後も業務拡大を目指しておりますので、折に触れコンペを開催させていただくつもりですので、引き続きよろしくお願いいたします。

```html
<!DOCTYPE html>
<html lang="ja">
<head>
<meta charset="utf-8">
<title>クロベリアルティ 事務所サイン</title>
<link rel="stylesheet" href="https://fonts.googleapis.com/css2?family=Noto+Sans+JP:wght@700;900&family=Noto+Serif:wght@500&display=swap">
<style>
  :root {
    --navy: #40607f;
    --silver: #c5c8cb;
    --orange: #ef8a1d;
    --white: #ffffff;
  }
  html, body {
    margin: 0;
    padding: 0;
    width: 1200px;
    height: 3700px;
    overflow: hidden;
    background: var(--silver);
  }
  .sign {
    position: relative;
    width: 1200px;
    height: 3700px;
    background: var(--silver);
    overflow: hidden;
  }
  .sign__backdrop {
    position: absolute;
    inset: 0;
  }
  .brand {
    position: absolute;
    top: 0;
    left: 0;
    width: 1200px;
    height: 740px;
    display: flex;
    flex-direction: column;
    align-items: center;
  }
  .brand__dot {
    margin-top: 150px;
    width: 250px;
    height: 250px;
    border-radius: 50%;
    background: var(--orange);
  }
  .brand__name {
    margin-top: 120px;
    font-family: "Noto Serif", serif;
    font-weight: 500;
    font-size: 54px;
    letter-spacing: 3px;
    color: var(--white);
    white-space: nowrap;
  }
  .office-name {
    position: absolute;
    top: 1180px;
    left: 410px;
    writing-mode: vertical-rl;
    font-family: "Noto Sans JP", sans-serif;
    font-weight: 900;
    font-size: 190px;
    line-height: 1;
    letter-spacing: 6px;
    color: var(--navy);
    white-space: nowrap;
  }
  .office-services {
    position: absolute;
    top: 1200px;
    left: 722px;
    writing-mode: vertical-rl;
    font-family: "Noto Sans JP", sans-serif;
    font-weight: 700;
    font-size: 108px;
    line-height: 1;
    letter-spacing: 0;
    color: var(--navy);
    white-space: nowrap;
  }
  .parking-guide {
    position: absolute;
    left: 0;
    top: 3280px;
  }
</style>
</head>
<body>
  <main class="sign">
    <svg class="sign__backdrop" width="1200" height="3700" viewBox="0 0 1200 3700" aria-hidden="true">
      <polygon points="0,0 1200,0 1200,1220 0,760" fill="var(--navy)"/>
    </svg>

    <header class="brand">
      <div class="brand__dot"></div>
      <div class="brand__name">KUROBE REALTY</div>
    </header>

    <h1 class="office-name">クロベ　リアルティ</h1>
    <p class="office-services" style="margin:0">行政書士／土地家屋調査士　事務所</p>

    <svg class="parking-guide" width="1200" height="300" viewBox="0 0 1200 300" role="img" aria-label="駐車場は左方向">
      <g fill="none" stroke="var(--navy)" stroke-width="44" stroke-linecap="round" stroke-linejoin="round">
        <line x1="325" y1="140" x2="485" y2="140"/>
        <polyline points="395,55 310,140 395,225"/>
      </g>
      <circle cx="760" cy="140" r="112" fill="var(--navy)"/>
      <text x="760" y="140" dy="0.35em" text-anchor="middle" font-family="Noto Sans JP, sans-serif" font-weight="900" font-size="150" fill="var(--white)">P</text>
    </svg>
  </main>
</body>
</html>
```